Update New Business Card - For Start Up

I need to update my business card, I have our old version for example. I would like to keep to the same colors and theme. We are a threat reporting and case management tool for corporations and educational institutions.

Target Market(s)

Corporate Security and Human Resources, School Administrators and Superintendents.

Industry/Entity Type

Physical Security and Technology.

Contact Information for Business Card

My Name, Founder/CEO, phone number 777-412-5068, Logo, Web...

Colors
0054AA
0677BA
7BADD7
CADEEF
E8F1F8

Requirements
Must have
• Something new and trendy.

```html
<!DOCTYPE html>
<html lang="en">
<head>
<meta charset="utf-8">
<title>Vantrel Business Card</title>
<link rel="stylesheet" href="https://fonts.googleapis.com/css2?family=Arimo:wght@400;700&display=swap">
<style>
  :root {
    --backdrop: #c4c4c4;
    --card: #181818;
    --brand-blue: #1f73bd;
    --edge-blue: #0677ba;
    --text-light: #f2f2f2;
    --rule: #0054aa;
  }
  * { box-sizing: border-box; margin: 0; padding: 0; }
  html, body {
    width: 1200px; height: 800px; overflow: hidden;
    background: var(--backdrop);
    font-family: "Arimo", Arial, sans-serif;
  }
  .canvas {
    width: 1200px; height: 800px;
    display: flex; align-items: center; justify-content: center; gap: 40px;
  }
  .card {
    width: 540px; height: 309px;
    background: var(--card);
    border: 1px solid var(--edge-blue);
    border-radius: 2px;
    position: relative;
  }
  .brand {
    display: flex; align-items: center;
    color: var(--brand-blue);
    font-weight: 700;
    text-transform: uppercase;
  }
  .brand-dot {
    border-radius: 50%;
    background: var(--brand-blue);
    flex: none;
  }
  /* Front */
  .card-front .brand {
    position: absolute; left: 40px; top: 50%; transform: translateY(-50%);
    font-size: 30px; letter-spacing: 5px; gap: 12px;
  }
  .card-front .brand-dot { width: 44px; height: 44px; }
  .divider {
    position: absolute; left: 292px; top: 78px;
    width: 1px; height: 150px; background: var(--rule);
  }
  .contact {
    position: absolute; left: 314px; top: 66px;
    color: var(--text-light);
  }
  .person-name {
    color: var(--brand-blue);
    font-weight: 700; font-size: 19px; letter-spacing: 1.5px;
    text-transform: uppercase;
  }
  .person-title { font-size: 15px; margin-top: 3px; }
  .contact-list { list-style: none; margin-top: 20px; }
  .contact-list li {
    display: flex; align-items: center; gap: 10px;
    font-size: 14px; margin-bottom: 9px;
  }
  .contact-icon { width: 20px; height: 20px; flex: none; }
  /* Back */
  .card-back .brand {
    position: absolute; left: 50%; top: 50%; transform: translate(-50%, -50%);
    font-size: 40px; letter-spacing: 7px; gap: 16px;
  }
  .card-back .brand-dot { width: 60px; height: 60px; }
</style>
</head>
<body>
<main class="canvas">
  <section class="card card-front">
    <div class="brand"><span class="brand-dot"></span>Vantrel</div>
    <div class="divider"></div>
    <div class="contact">
      <p class="person-name">Dario Kessling</p>
      <p class="person-title">Founder / CEO</p>
      <ul class="contact-list">
        <li>
          <svg class="contact-icon" viewBox="0 0 20 20" aria-hidden="true">
            <circle cx="10" cy="10" r="10" fill="#1f73bd"/>
            <path d="M5.5 9.5c2.5-2.6 6.5-2.6 9 0l-1.4 1.3-1.6-1v-1.2c-1-.4-2-.4-3 0v1.2l-1.6 1z" fill="#fff"/>
            <rect x="7.5" y="11" width="5" height="3" rx="1" fill="#fff"/>
          </svg>
          <span>777-412-5068</span>
        </li>
        <li>
          <svg class="contact-icon" viewBox="0 0 20 20" aria-hidden="true">
            <circle cx="10" cy="10" r="10" fill="#1f73bd"/>
            <rect x="5" y="6.5" width="10" height="7" fill="#fff"/>
            <path d="M5 6.5l5 4 5-4" fill="none" stroke="#1f73bd" stroke-width="1"/>
          </svg>
          <span>dario@vantrel.co</span>
        </li>
        <li>
          <svg class="contact-icon" viewBox="0 0 20 20" aria-hidden="true">
            <circle cx="10" cy="10" r="10" fill="#1f73bd"/>
            <g fill="none" stroke="#fff" stroke-width="1">
              <circle cx="10" cy="10" r="5"/>
              <ellipse cx="10" cy="10" rx="2.2" ry="5"/>
              <path d="M5 10h10M6 7.5h8M6 12.5h8"/>
            </g>
          </svg>
          <span>www.vantrel.co</span>
        </li>
      </ul>
    </div>
  </section>
  <section class="card card-back">
    <div class="brand"><span class="brand-dot"></span>Vantrel</div>
  </section>
</main>
</body>
</html>
```